Need Catering Menu designed - design that we want is attached

Hi,
We need a new catering menu designed for our cafe.
I have attached our coffee menu, we would like it to follow the same kind of layout.
It needs to be A4, and can be double sided.
I have attached a word doc of our catering menu, so this is what needs to be on the catering menu you produce.
Also, our contact details need to be on both sides of the menu:
Visit us instore to discuss catering options, or call 0438 672 914 or email marla@tevrostudio.com.au
I have also attached our new logo which I'd like incorporated into the menu
Target Market(s)
Doctors/Nurses
Hospital staff
University Students
Industry/Entity Type
Catering
Look and feel

```html
<!DOCTYPE html>
<html lang="en">
<head>
<meta charset="utf-8">
<title>Ward Nine Catering Menu</title>
<link href="https://fonts.googleapis.com/css2?family=Open+Sans:ital,wght@0,400;0,600;0,700;1,700&display=swap" rel="stylesheet">
<style>
  :root {
    --canvas: #ffffff;
    --page-top: #e9e4dd;
    --page-bottom: #f1eee9;
    --bean-dark: #4a2c17;
    --bean-mid: #8a5a33;
    --panel: rgba(58, 40, 30, 0.86);
    --accent: #c9622b;
    --text-light: #f3ece4;
    --text-dark: #3d2a1e;
    --skin: #d9b59a;
  }
  * { margin: 0; padding: 0; box-sizing: border-box; }
  html, body { width: 800px; height: 1200px; overflow: hidden; background: var(--canvas); }
  body { position: relative; font-family: "Open Sans", Arial, sans-serif; color: var(--text-light); }

  .page { position: absolute; left: 20px; width: 760px; height: 540px; overflow: hidden; }
  .page--breakfast { top: 24px; background: var(--page-top); }
  .page--lunch { top: 630px; background: var(--page-bottom); }

  .beans-photo { position: absolute; left: 0; right: 0; bottom: 0; height: 300px;
    background: linear-gradient(180deg, rgba(138,90,51,0) 0%, var(--bean-mid) 35%, var(--bean-dark) 100%); }
  .lunch-photo { position: absolute; right: 0; top: 0; width: 430px; height: 100%;
    background: linear-gradient(100deg, rgba(241,238,233,0) 0%, #e5d3c3 25%, var(--skin) 60%, #b98a6a 100%); }

  .brand { position: absolute; left: 0; right: 0; top: 18px; text-align: center; color: var(--text-dark); }
  .brand__name { display: inline-flex; align-items: center; gap: 8px; font-weight: 700; font-size: 20px; letter-spacing: 2px; text-transform: uppercase; }
  .brand__dot { width: 14px; height: 14px; border-radius: 50%; background: var(--accent); }
  .brand__tagline { margin-top: 12px; font-size: 10px; font-weight: 600; letter-spacing: 3px; }
  .brand__tagline::before, .brand__tagline::after { content: ""; display: inline-block; width: 200px; height: 1px; background: var(--text-dark); vertical-align: middle; margin: 0 12px; opacity: .5; }

  .panel { position: absolute; background: var(--panel); padding: 40px 22px 14px; }
  .panel__tab { position: absolute; top: -14px; left: 20px; background: var(--accent); color: #fff; font-weight: 700; font-size: 12px; letter-spacing: 1px; padding: 6px 18px; border-radius: 14px; text-transform: uppercase; line-height: 1.1; }
  .menu { list-style: none; font-size: 10.5px; }
  .menu li { display: flex; justify-content: space-between; line-height: 19px; }
  .menu--small { font-size: 8px; }
  .menu--small li { line-height: 12.5px; display: block; }
  .menu__group { color: var(--accent); font-weight: 700; margin-top: 6px; }
  .menu__name { font-weight: 700; }
  .note { font-size: 8px; margin-top: 10px; line-height: 13px; opacity: .9; }

  .footer { position: absolute; left: 0; right: 0; bottom: 12px; text-align: center; color: var(--accent); font-weight: 700; font-style: italic; font-size: 11px; line-height: 15px; text-transform: uppercase; }
  .page--breakfast .footer { color: #f0a36c; }
</style>
</head>
<body>

<section class="page page--breakfast">
  <div class="beans-photo" role="img" aria-label="Photo of roasted coffee beans"></div>
  <header class="brand">
    <div class="brand__name"><span class="brand__dot"></span>Ward Nine</div>
    <div class="brand__tagline">COFFEE – CATERING – FOOD TO GO</div>
  </header>

  <div class="panel" style="left:40px; top:115px; width:320px; height:340px;">
    <div class="panel__tab">Hot Beverage</div>
    <ul class="menu">
      <li><span>Fruit Platter</span><span>$5</span></li>
      <li><span>Bacon Egg and Cheese Roll</span><span>$6.5</span></li>
      <li><span>Vegetarian Brekky Wrap</span><span>$6.5</span></li>
      <li><span>Ham and Cheese Croissant</span><span>$6</span></li>
      <li><span>Cheese and Tomato Croissant</span><span>$6</span></li>
      <li><span>Ham and Cheese French Toast</span><span>$6.5</span></li>
      <li><span>Assorted Yoghurts</span><span>$5.5</span></li>
      <li><span>Bircher Muesli</span><span>$5.5</span></li>
      <li><span>Chia Pudding</span><span>$5.5</span></li>
      <li><span>Granola and Yoghurt</span><span>$5.5</span></li>
      <li><span>Muffins</span><span>$4.5</span></li>
      <li><span>Mini Muffins</span><span>$2.5</span></li>
      <li><span>Juice</span><span>$4</span></li>
    </ul>
  </div>

  <div class="panel" style="left:400px; top:115px; width:320px; height:340px;">
    <div class="panel__tab">Morning and<br>Afternoon Tea</div>
    <ul class="menu">
      <li><span>Fruit Platter</span><span>$5</span></li>
      <li><span>Muffins</span><span>$4.5</span></li>
      <li><span>Mini Muffins</span><span>$2.5</span></li>
      <li><span>Assorted Slices</span><span>$4</span></li>
      <li><span>Assorted Cookies from</span><span>$3</span></li>
      <li><span>Assorted Yoghurts</span><span>$5.5</span></li>
      <li><span>Chia Pudding</span><span>$5.5</span></li>
      <li><span>Banana Bread</span><span>$4.5</span></li>
      <li><span>Juice</span><span>$4</span></li>
    </ul>
    <p class="note">*Cups/Plates/Serviettes can be provided at a charge of $1 per person<br>*Barista made coffee available</p>
  </div>

  <p class="footer">Visit us instore to discuss catering options<br>or call 0438 672 914 or email marla@tevrostudio.com.au</p>
</section>

<section class="page page--lunch">
  <div class="lunch-photo" role="img" aria-label="Photo of a person enjoying a sandwich"></div>
  <header class="brand">
    <div class="brand__name"><span class="brand__dot"></span>Ward Nine</div>
    <div class="brand__tagline">COFFEE – CATERING – FOOD TO GO</div>
  </header>

  <div class="panel" style="left:20px; top:115px; width:320px; height:370px; padding-top:32px;">
    <div class="panel__tab">Lunch</div>
    <ul class="menu menu--small">
      <li class="menu__group">Sandwiches or Wraps $7.50</li>
      <li><span class="menu__name">Ham:</span> ham, cheese, tomato, lettuce, mustard</li>
      <li><span class="menu__name">Turkey:</span> turkey, cranberry, brie, spinach</li>
      <li><span class="menu__name">Chicken:</span> chicken, avocado, lettuce, mayo</li>
      <li><span class="menu__name">Salad:</span> cheese, carrot, beetroot, lettuce, tomato</li>
      <li><span class="menu__name">Tuna:</span> tuna, sweetcorn, lettuce, lemon mayo</li>
      <li><span class="menu__name">Egg:</span> egg, lettuce, chives, mayo</li>
      <li><span class="menu__name">Beef:</span> roast beef, tomato, onion, mustard</li>
      <li><span class="menu__name">Salami:</span> salami, cheese, tomato, spinach</li>
      <li class="menu__group">Focaccias $8.50</li>
      <li><span class="menu__name">Chicken Pesto:</span> chicken, pesto, tomato, mozzarella</li>
      <li><span class="menu__name">Veggie:</span> roast vegetables, feta, spinach</li>
      <li><span class="menu__name">Ham:</span> ham, cheese, tomato, onion</li>
      <li class="menu__group">Salads $9.50</li>
      <li><span class="menu__name">Greek:</span> feta, olives, cucumber, tomato, onion</li>
      <li><span class="menu__name">Chicken Caesar:</span> chicken, cos, bacon, croutons, parmesan</li>
    </ul>
  </div>

  <div class="panel" style="left:420px; top:115px; width:300px; height:370px; padding-top:30px;">
    <div class="panel__tab">Hot Food</div>
    <ul class="menu">
      <li><span>Assorted Pies</span><span>$5.0</span></li>
      <li><span>Large tray hot chips</span><span>$15</span></li>
      <li><span>Small tray hot chips</span><span>$9</span></li>
      <li><span>Mini samosa</span><span>$1</span></li>
      <li><span>Vegetarian spring rolls</span><span>$1</span></li>
      <li><span>Party pies</span><span>$2</span></li>
      <li><span>Mini sausage rolls</span><span>$1</span></li>
      <li><span>Mini quiche</span><span>$2</span></li>
      <li><span>Mini dim sim</span><span>$1</span></li>
      <li><span>Sweet chilli chicken tenders</span><span>$1</span></li>
      <li><span>Chicken tenders</span><span>$2</span></li>
      <li><span>Spinach and ricotta pastizzi</span><span>$3</span></li>
      <li><span>Vegetarian frittata</span><span>$4.5</span></li>
      <li><span>Meat frittata</span><span>$4.5</span></li>
    </ul>
  </div>

  <p class="footer">Visit us instore to discuss catering options<br>or call 0438 672 914 or email marla@tevrostudio.com.au</p>
</section>

</body>
</html>
```